Tri-Fold Brochure Redesign for Floral Preservation Business

I would like to redesign my current tri-fold brouchue that I created myself and have it updated. I would like to keep the same content, color and images, but have it redesigned to look fresher and updated. I'm in the the floral preservation business and work with brides in the wedding inductry. I'm looking for a royal/rustic feel and it should relate to the look and feel of my website www.larkmeadowbloom.com. I have included the Photoshop file I used to create my orginal bouchure.

The only content that has changed is my address which is now;
4827 Maple Brook Lane, Reston VA 20194

Safe Zone Width - 10.875
Safe Zone Height - 8.375

I have included the Photoshop and Illustrator templates for the tri-fold brochure from the printer I will be using.

```html
<!DOCTYPE html>
<html lang="en">
<head>
<meta charset="utf-8">
<title>Lark Meadow – Floral Preservation Tri-Fold</title>
<link rel="stylesheet" href="https://fonts.googleapis.com/css2?family=Cinzel:wght@400;600;700&family=Open+Sans:wght@400;600&display=swap">
<style>
  :root {
    --stage: #e6e6e6;
    --paper: #ffffff;
    --paper-shade: #e9e9e9;
    --ink: #3a3a3a;
    --crimson: #b3122e;
    --gold-light: #f6e7b4;
    --gold: #d9b866;
    --gold-deep: #a9812f;
    --header-ink: #3b2a0c;
    --wood-dark: #4a140e;
    --wood: #7a2a1c;
    --mat: #e8dcc0;
    --mat-inner: #f3ecda;
    --bead-blue: #4fa9d6;
    --bead-light: #a6d7ee;
    --silver: #b9b9b9;
    --night: #0c0c0c;
    --night-soft: #3a3a3a;
    --night-text: #e9e9e9;
    --heading-grey: #c9c9c9;
  }
  * { box-sizing: border-box; margin: 0; padding: 0; }
  html, body { width: 1200px; height: 1080px; overflow: hidden; }
  body {
    background: radial-gradient(ellipse at center, #f7f7f7 0%, var(--stage) 75%);
    font-family: "Open Sans", Arial, sans-serif;
    color: var(--ink);
  }
  .brochure {
    position: absolute;
    left: 36px; top: 92px;
    width: 1128px; height: 896px;
    display: flex;
    box-shadow: 0 18px 40px rgba(0,0,0,.18);
  }
  .panel { position: relative; width: 376px; height: 100%; }
  .panel--preservation { background: var(--paper); }
  .panel--jewelry { background: linear-gradient(90deg, var(--paper-shade) 0%, var(--paper) 55%); }
  .panel--process {
    background: linear-gradient(160deg, var(--night-soft) 0%, var(--night) 45%, #1c1c1c 100%);
    border-left: 4px solid var(--crimson);
    color: var(--night-text);
    text-align: center;
    padding: 26px 26px 0;
  }
  .tagline-band {
    position: absolute; left: 0; top: 0; width: 752px; height: 88px; z-index: 2;
    background: linear-gradient(180deg, var(--gold-light) 0%, var(--gold) 55%, #efd894 100%);
    display: flex; align-items: center; justify-content: center;
    padding: 0 56px;
  }
  .tagline {
    font-family: "Cinzel", Georgia, serif;
    font-weight: 600;
    font-size: 15.5px;
    line-height: 1.4;
    text-align: center;
    color: var(--header-ink);
    letter-spacing: .3px;
  }
  .shadowbox {
    position: absolute;
    left: 42px; top: 124px; width: 256px; height: 340px;
    border: 14px solid var(--wood);
    border-top-color: var(--wood-dark);
    border-left-color: var(--wood-dark);
    background: var(--mat);
    padding: 20px;
    box-shadow: 4px 6px 12px rgba(0,0,0,.3);
  }
  .shadowbox-art {
    width: 100%; height: 100%;
    background: radial-gradient(ellipse at 50% 40%, #fbf7ea 0%, var(--mat-inner) 55%, #e4d7b6 100%);
    box-shadow: inset 0 0 0 2px #cdbd94;
  }
  .bracelet {
    position: absolute;
    left: 36px; top: 150px; width: 304px; height: 250px;
    border-radius: 50%;
    background: radial-gradient(ellipse at center, rgba(255,255,255,0) 38%, var(--bead-light) 46%, var(--bead-blue) 56%, var(--silver) 64%, rgba(255,255,255,0) 72%);
  }
  .panel-heading {
    position: absolute; left: 22px; right: 22px; top: 508px;
    font-family: "Cinzel", Georgia, serif;
    font-weight: 400;
    font-size: 25px;
    color: var(--crimson);
  }
  .panel-copy {
    position: absolute; left: 22px; right: 24px; top: 554px;
    font-size: 13.6px;
    line-height: 1.55;
    text-align: justify;
  }
  .process-title {
    font-family: "Cinzel", Georgia, serif;
    font-weight: 600;
    font-size: 30px;
    color: #fff;
    margin-bottom: 20px;
  }
  .step { margin-bottom: 24px; }
  .step-badge {
    display: inline-block;
    font-family: "Cinzel", Georgia, serif;
    font-weight: 700;
    font-size: 20px;
    color: var(--header-ink);
    padding: 4px 26px;
    border-radius: 18px;
    background: linear-gradient(180deg, var(--gold-light) 0%, var(--gold) 55%, var(--gold-deep) 100%);
  }
  .step-flourish {
    display: block;
    width: 58px; height: 8px;
    margin: 6px auto 6px;
    background: linear-gradient(90deg, rgba(255,255,255,0), #f0f0f0, rgba(255,255,255,0));
    border-radius: 4px;
  }
  .step-heading {
    font-family: "Cinzel", Georgia, serif;
    font-weight: 400;
    font-size: 21px;
    color: var(--heading-grey);
    margin-bottom: 6px;
  }
  .step-copy {
    font-size: 13.2px;
    line-height: 1.5;
    text-align: justify;
    text-align-last: center;
  }
  .process-footer {
    font-size: 13.2px;
    line-height: 1.6;
    margin-top: 22px;
  }
</style>
</head>
<body>
  <main class="brochure">
    <div class="tagline-band">
      <p class="tagline">You Have Chosen The Perfect Flowers. Now Choose The Perfect Way To Cherish Them. Lark Meadow's Floral Preservation Process Transforms Your Flowers Into Lasting Works of Art or Jewelry</p>
    </div>

    <section class="panel panel--preservation">
      <div class="shadowbox">
        <div class="shadowbox-art" role="img" aria-label="Preserved bridal bouquet mounted inside the shadowbox"></div>
      </div>
      <h2 class="panel-heading">Floral Preservation</h2>
      <p class="panel-copy">Our handcrafted shadowboxes are made with the industries finest raw materials to ensure the highest level of quality. We exclusively offer Hollis-Grant moulding, makers of beautiful moulding for over 100 years. Using archival standards set by the Halloway Archive Council, our shadowboxes are matted and mounted with the Brightwell FrameCare system. This system is used by museums to protect some of this nation's most valuable artwork. We finish by using ClearVista's Gallery glass to enhance, protect and beautify. Each of these details contributes to a museum-quality work of art.</p>
    </section>

    <section class="panel panel--jewelry">
      <div class="bracelet" role="img" aria-label="Silver bracelet with blue flower-petal beads and pearls"></div>
      <h2 class="panel-heading">Flower-Petal Jewelry</h2>
      <p class="panel-copy">If you would like to turn your memories into a wearable story, consider creating signature jewelry. We turn real petals from your blooms into one-of-a-kind jewelry pieces for you or your loved ones. We can transform your flowers into earrings, necklaces, bracelets, Linden- and Fable-type charms or rosaries. The tradition hails from the historical practice of nuns creating rosaries from condensed flower petals. In that same vein, we create unique pieces to fit your own style. Each piece is made by hand from your flowers and the highest quality sterling silver findings.</p>
    </section>

    <section class="panel panel--process">
      <h2 class="process-title">The Process</h2>

      <div class="step">
        <span class="step-badge">Step 1</span>
        <span class="step-flourish" role="img" aria-label="Small white flourish ornament"></span>
        <h3 class="step-heading">Reserve The Date</h3>
        <p class="step-copy">To ensure our services, you will need to "reserve the date" with a deposit. We accept no more than 4 clients a week and with over 50,000 weddings in the DC and Hampton Roads Metro areas annually, many brides reserve their wedding date up to four months in advance. The full deposit is applied to the cost of your final design selection.</p>
      </div>

      <div class="step">
        <span class="step-badge">Step 2</span>
        <span class="step-flourish" role="img" aria-label="Small white flourish ornament"></span>
        <h3 class="step-heading">Secure The Flowers</h3>
        <p class="step-copy">You can either drop your flowers off shortly after the event, or we can pick them up the night of the reception. Is your event out of town? No problem. You can ship them to us overnight or drop them off upon your return.</p>
      </div>

      <div class="step">
        <span class="step-badge">Step 3</span>
        <span class="step-flourish" role="img" aria-label="Small white flourish ornament"></span>
        <h3 class="step-heading">Design Selection</h3>
        <p class="step-copy">Within 30 days after your event we ask that you make an appointment to visit our showroom to make your final design selection. Once your order has been placed, it takes approximately 2 to 3 months to complete.</p>
      </div>

      <p class="process-footer">Please visit our website for full details,<br>pricing and additional pictures.<br>www.larkmeadowbloom.com<br>4827 Maple Brook Lane, Reston VA 20194</p>
    </section>
  </main>
</body>
</html>
```